Design a website for our small self storage business

We're looking for a freelance web designer who can produce a good-looking design for our small business website (no coding necessary). We will provide a list of pages to design, along with content outlines.

Key skills:
- Graphic design
- Responsive web design
- Proficiency with a modern web design tool such as Figma, Adobe Xd, or InVision

Please send relevant previous work (preferably in an inspectable format such as Figma or Invision).

```html
<!DOCTYPE html>
<html lang="en">
<head>
<meta charset="utf-8">
<title>Harbor Lane Storage</title>
<link href="https://fonts.googleapis.com/css2?family=Inter:wght@400;500;600;700;800;900&display=swap" rel="stylesheet">
<style>
:root{
  --red:#e31e24;
  --navy:#004a85;
  --grey:#666a70;
  --white:#ffffff;
  --soft:#f1f2f4;
}
*{margin:0;padding:0;box-sizing:border-box}
html,body{width:713px;height:1200px;overflow:hidden;background:var(--white)}
body{font-family:"Inter",sans-serif;position:relative;color:var(--grey)}
.abs{position:absolute}
.brand{left:107px;top:58px;display:flex;align-items:center;gap:5px}
.brand-mark{width:11px;height:11px;background:var(--red)}
.brand-name{font-size:11px;font-weight:800;color:var(--navy);letter-spacing:.3px;line-height:1.05}
.nav{top:64px;font-size:7px;color:var(--navy)}
.nav a{position:absolute;color:var(--navy);text-decoration:none;white-space:nowrap}
.nav a.active{color:var(--red)}
.nav a.active::after{content:"";position:absolute;left:0;right:0;top:12px;height:1px;background:var(--red)}
.hero{left:51px;top:95px;width:611px;height:293px;overflow:hidden}
.hero-photo{position:absolute;inset:0;background:linear-gradient(90deg,#2a2b3a 0%,#8a6e4e 18%,#c9c5c2 40%,#6d7b93 50%,#cfc9c3 60%,#8b6b4c 82%,#2c2d3b 100%)}
.hero-bands{position:absolute;inset:0}
.hero-card{left:202px;top:176px;width:312px;height:123px;background:rgba(244,245,247,.94);border-radius:24px;text-align:center}
.hero-title{margin-top:20px;font-size:28px;font-weight:900;letter-spacing:2.2px;color:var(--navy);line-height:1}
.hero-title span{color:var(--red)}
.hero-text{margin-top:8px;font-size:5.6px;line-height:12px;color:var(--navy)}
.btn{display:inline-block;margin-top:5px;width:84px;height:21px;line-height:21px;border-radius:11px;background:var(--red);color:var(--white);font-size:8.5px;font-weight:700}
.section-title{left:0;width:713px;text-align:center;font-size:18px;font-weight:900;letter-spacing:1.8px;color:var(--navy)}
.section-title span{color:var(--red)}
.sub{left:0;width:713px;text-align:center;font-size:5.6px;line-height:11.7px}
.card{top:496px;width:126px;height:157px;border:1.2px solid var(--red);border-radius:12px;text-align:center}
.card-icon{width:44px;height:44px;border-radius:50%;background:var(--soft);margin:14px auto 0;display:flex;align-items:center;justify-content:center}
.card-title{margin-top:9px;font-size:9px;font-weight:600;color:var(--navy)}
.card-text{margin-top:8px;font-size:5.6px;line-height:11.7px}
.card-link{margin-top:9px;font-size:5.8px;color:var(--red)}
.faq{left:51px;top:698px;width:611px;height:272px;overflow:hidden}
.faq-photo{position:absolute;inset:0;background:linear-gradient(180deg,#d63a44 0%,#e2414a 45%,#c21f27 80%,#d8343d 100%)}
.faq-title{left:0;width:713px;top:767px;text-align:center;font-size:17px;font-weight:800;letter-spacing:1.5px;color:var(--white)}
.accordion{left:187px;top:817px;width:340px;height:71px;border:1px solid var(--white);border-radius:4px;overflow:hidden}
.acc-head{height:26px;background:var(--white);display:flex;align-items:center;justify-content:space-between;padding:0 13px 0 17px;font-size:7px;font-weight:600;color:var(--navy)}
.acc-body{padding:10px 17px;font-size:5.6px;line-height:11.7px;color:var(--white)}
.foot-head{top:1017px;font-size:7px;font-weight:600;color:var(--navy)}
.hours{left:127px;top:1041px;font-size:5.6px;line-height:11.8px}
.hours div{display:flex}
.hours span:first-child{width:46px}
.copyright{left:0;width:713px;top:1028px;text-align:center;font-size:5.6px}
.foot-brand{left:0;width:713px;top:1064px;display:flex;justify-content:center;align-items:center;gap:5px}
.foot-nav a{position:absolute;top:1109px;font-size:5.8px;color:var(--grey);text-decoration:none}
.contact-row{left:500px;display:flex;gap:6px;font-size:5.6px;line-height:11.7px}
</style>
</head>
<body>

<div class="abs brand"><div class="brand-mark"></div><div class="brand-name">Harbor Lane</div></div>

<nav class="abs nav" style="left:0">
  <a class="active" style="left:423px">Home</a>
  <a style="left:462px">About</a>
  <a style="left:501px">Services</a>
  <a style="left:549px">FAQ</a>
  <a style="left:582px">Contact</a>
</nav>

<section class="abs hero">
  <div class="hero-photo" role="img" aria-label="Photo of a warehouse aisle with tall shelves stacked with boxes"></div>
  <svg class="hero-bands" width="611" height="293" viewBox="0 0 611 293">
    <polygon points="0,288 302,261 611,283 611,290 302,273 0,293" fill="#e31e24"/>
    <polygon points="0,293 302,273 611,290 611,293" fill="#fff"/>
  </svg>
</section>

<div class="abs hero-card">
  <h1 class="hero-title"><span>SELF</span> STORAGE</h1>
  <p class="hero-text">Lorem ipsum dolor sit amet, consectetur adipiscing elit.<br>Nullam dictum mi sit amet ullamcorper ultricies. Maecenas commodo accumsan ultrices.</p>
  <span class="btn">HOME</span>
</div>

<h2 class="abs section-title" style="top:416px">WHAT WE <span>OFFER</span></h2>
<p class="abs sub" style="top:450px">Lorem ipsum dolor sit amet, consectetur adipiscing elit.<br>Nullam dictum mi sit amet</p>

<div class="abs card" style="left:138px">
  <div class="card-icon"><svg width="22" height="18" viewBox="0 0 22 18"><rect x="1" y="1" width="20" height="12" rx="1" fill="#cfe6f5" stroke="#8aa" stroke-width=".8"/><rect x="4" y="4" width="6" height="6" fill="#c98a4b"/><rect x="12" y="4" width="7" height="1.2" fill="#456"/><rect x="12" y="7" width="6" height="1.2" fill="#456"/><rect x="9" y="13" width="4" height="3" fill="#aaa"/><rect x="6" y="16" width="10" height="1.2" fill="#bbb"/></svg></div>
  <h3 class="card-title">Drive-Up Spaces</h3>
  <p class="card-text">Lorem ipsum dolor sit<br>amet, consectetur adipiscing elit.<br>Nullam dictum mi sit amet</p>
  <p class="card-link">View More</p>
</div>
<div class="abs card" style="left:293px">
  <div class="card-icon"><svg width="22" height="22" viewBox="0 0 22 22"><polygon points="2,8 11,2 20,8 20,21 2,21" fill="#e0474d"/><rect x="6" y="10" width="10" height="11" fill="#ddd"/><rect x="8" y="15" width="6" height="6" fill="#c98a4b"/></svg></div>
  <h3 class="card-title">Self Storage</h3>
  <p class="card-text">Lorem ipsum dolor sit<br>amet, consectetur adipiscing elit.<br>Nullam dictum mi sit amet</p>
  <p class="card-link">View More</p>
</div>
<div class="abs card" style="left:448px">
  <div class="card-icon"><svg width="24" height="20" viewBox="0 0 24 20"><rect x="2" y="1" width="2" height="19" fill="#777"/><rect x="20" y="1" width="2" height="19" fill="#777"/><rect x="2" y="8" width="20" height="1.6" fill="#777"/><rect x="2" y="16" width="20" height="1.6" fill="#777"/><rect x="6" y="2" width="5" height="6" fill="#c98a4b"/><rect x="13" y="3" width="5" height="5" fill="#c98a4b"/><rect x="9" y="11" width="7" height="5" fill="#c98a4b"/></svg></div>
  <h3 class="card-title">Small Business</h3>
  <p class="card-text">Lorem ipsum dolor sit<br>amet, consectetur adipiscing elit.<br>Nullam dictum mi sit amet</p>
  <p class="card-link">View More</p>
</div>

<section class="abs faq">
  <div class="faq-photo" role="img" aria-label="Photo of a storage facility building with roll-up doors, tinted red"></div>
  <svg class="abs" style="left:0;top:0" width="611" height="272" viewBox="0 0 611 272">
    <polygon points="0,0 611,0 611,3 302,20 0,0" fill="#fff"/>
    <polygon points="0,0 302,20 611,3 611,6 302,31 0,3" fill="#004a85"/>
    <polygon points="0,3 302,31 611,6 611,8 302,33 0,5" fill="#fff"/>
    <polygon points="0,266 302,241 611,264 611,269 302,252 0,272" fill="#004a85"/>
    <polygon points="0,272 302,252 611,269 611,272" fill="#fff"/>
  </svg>
</section>

<h2 class="abs faq-title">FAQ</h2>
<div class="abs accordion">
  <div class="acc-head"><span>What should I bring to rent a space?</span>
    <svg width="6" height="4" viewBox="0 0 6 4"><polyline points="0.5,0.5 3,3 5.5,0.5" fill="none" stroke="#004a85" stroke-width=".8"/></svg></div>
  <p class="acc-body">Lorem ipsum dolor sit amet, consectetur adipiscing elit. Nullam dictum mi sit ametLorem ipsum dolor<br>sit amet, consectetur adipiscing elit. Nullam dictum mi sit amet</p>
</div>

<h4 class="abs foot-head" style="left:127px">Opening Times</h4>
<div class="abs hours">
  <div><span>Monday:</span><span>09 AM - 05 PM</span></div>
  <div><span>Tuesday:</span><span>09 AM - 05 PM</span></div>
  <div><span>Wednesday:</span><span>09 AM - 05 PM</span></div>
  <div><span>Thursday:</span><span>09 AM - 05 PM</span></div>
  <div><span>Friday:</span><span>09 AM - 05 PM</span></div>
  <div><span>Saturday:</span><span>Closed</span></div>
  <div><span>Sunday:</span><span>Closed</span></div>
</div>

<p class="abs copyright">© 2022 Harbor Lane Storage</p>
<div class="abs foot-brand"><div class="brand-mark"></div><div class="brand-name">Harbor Lane</div></div>
<nav class="foot-nav">
  <a style="left:286px">Home</a><a style="left:316px">About</a><a style="left:346px">Services</a><a style="left:383px">FAQ</a><a style="left:407px">Contact</a>
</nav>

<h4 class="abs foot-head" style="left:502px">Contact Details</h4>
<div class="abs contact-row" style="top:1041px;left:502px">
  <svg width="13" height="14" viewBox="0 0 13 14"><path d="M6.5 13 C2 8 1 6 1 5 A5.5 5 0 0 1 12 5 C12 6 11 8 6.5 13Z" fill="none" stroke="#004a85" stroke-width=".7"/><circle cx="6.5" cy="5" r="2.3" fill="none" stroke="#004a85" stroke-width=".7"/></svg>
  <span>48 Elm Road, Fairview,<br>CA 90210</span>
</div>
<div class="abs contact-row" style="top:1076px;left:502px;align-items:center">
  <svg width="13" height="13" viewBox="0 0 13 13"><path d="M3 1 L5 4 L4 5.5 C5 7.5 6 8.5 8 9.5 L9.5 8.5 L12 10.5 L10.5 12 C6 12 1 7 1 2.5Z" fill="none" stroke="#004a85" stroke-width=".7"/></svg>
  <span>(310) 482-7716.</span>
</div>

</body>
</html>
```